Zelno Vigor Iron Tempo Multi Vitamin Label Design

We need a label design for our Sports Performance Daily Multi Vitamin specially created and branded for our Zelno Vigor line for the University of Calvoria. The feel is edgy, sports nutrition. Two logos need to be incorporated... Zelno and the Collective Logo attached. The colors should be the official colors of the University of Calvoria. The font may also be the Georgia font... or the Zelno font. Or any font. A hydration product will also be created later on...so this label design may be used on many products. Please utilize the collective logo similar to the use in the attached photo. No official trademark items from the University of Calvoria should be used. Attached is also an image if the bottle (white) that will be used for the vitamin. Please use red, black, grey, white. We are looking for the front design only right now and once selected, will work on the nutrition/back label portion with the artist.

```html
<!DOCTYPE html>
<html lang="en">
<head>
<meta charset="utf-8">
<title>Zelno Vigor – Iron Tempo Label</title>
<link rel="stylesheet" href="https://fonts.googleapis.com/css2?family=Montserrat:wght@300;400;600;700;800&family=Permanent+Marker&display=swap">
<style>
  :root {
    --red: #a80d2c;
    --red-deep: #8a0c25;
    --red-sheen: #c63a56;
    --black: #161616;
    --white: #ffffff;
    --grey: #e6e6e6;
    --page: #ffffff;
  }
  html, body {
    margin: 0;
    width: 1200px;
    height: 1200px;
    overflow: hidden;
    background: var(--page);
  }
  .canvas {
    position: relative;
    width: 1200px;
    height: 1200px;
  }
  .label {
    position: absolute;
    left: 150px;
    top: 20px;
    width: 900px;
    height: 1160px;
    overflow: hidden;
    background: var(--red);
    font-family: "Montserrat", sans-serif;
    color: var(--white);
  }
  .label-shading {
    position: absolute;
    inset: 0;
  }
  .brand-name {
    position: absolute;
    left: 54px;
    top: 62px;
    margin: 0;
    font-weight: 800;
    font-size: 104px;
    line-height: 1;
    letter-spacing: 2px;
    color: var(--white);
  }
  .collective-badge {
    position: absolute;
    left: 652px;
    top: 56px;
    width: 204px;
    height: 204px;
    border-radius: 50%;
    background: var(--grey);
  }
  .product-title {
    position: absolute;
    left: 72px;
    top: 360px;
    margin: 0;
  }
  .product-title .title-main {
    display: block;
    font-family: "Permanent Marker", cursive;
    font-size: 210px;
    line-height: 1;
    color: var(--black);
    letter-spacing: -4px;
  }
  .product-title .title-sub {
    display: block;
    margin-top: -30px;
    font-weight: 800;
    font-size: 92px;
    line-height: 1;
    color: var(--white);
  }
  .product-type {
    position: absolute;
    left: 74px;
    top: 640px;
    margin: 0;
    font-weight: 600;
    font-size: 42px;
    color: var(--white);
  }
  .quality {
    position: absolute;
    left: 74px;
    top: 752px;
    margin: 0;
    font-weight: 300;
    font-size: 42px;
    letter-spacing: 1px;
    color: var(--white);
  }
  .quality-stars {
    position: absolute;
    left: 76px;
    top: 812px;
    display: flex;
    gap: 8px;
  }
  .count-badge {
    position: absolute;
    left: 72px;
    top: 957px;
    width: 120px;
    height: 120px;
    border-radius: 50%;
    background: var(--black);
    display: flex;
    flex-direction: column;
    align-items: center;
    justify-content: center;
    color: var(--white);
  }
  .count-badge .count-number {
    font-weight: 800;
    font-size: 40px;
    line-height: 1;
  }
  .count-badge .count-unit {
    font-weight: 700;
    font-size: 22px;
    line-height: 1.1;
  }
  .supplement-note {
    position: absolute;
    left: 74px;
    top: 1110px;
    margin: 0;
    font-weight: 400;
    font-size: 20px;
    letter-spacing: 7px;
    color: var(--white);
  }
</style>
</head>
<body>
<div class="canvas">
  <section class="label">
    <svg class="label-shading" width="900" height="1160" viewBox="0 0 900 1160" aria-hidden="true">
      <defs>
        <linearGradient id="sheen-left" x1="0" y1="0" x2="1" y2="0">
          <stop offset="0" stop-color="#a80d2c"/>
          <stop offset="0.2" stop-color="#c63a56"/>
          <stop offset="0.35" stop-color="#a80d2c"/>
          <stop offset="1" stop-color="#a80d2c"/>
        </linearGradient>
        <linearGradient id="sheen-right" x1="0" y1="0" x2="1" y2="0">
          <stop offset="0" stop-color="#b43a52"/>
          <stop offset="0.3" stop-color="#8a0c25"/>
          <stop offset="0.65" stop-color="#8a0c25"/>
          <stop offset="0.86" stop-color="#b23d57"/>
          <stop offset="1" stop-color="#7c1a2e"/>
        </linearGradient>
      </defs>
      <rect width="900" height="1160" fill="url(#sheen-left)"/>
      <polygon points="900,0 900,1160 0,1160" fill="url(#sheen-right)"/>
    </svg>

    <h2 class="brand-name">Zelno</h2>
    <div class="collective-badge" role="img" aria-label="Collective partner badge"></div>

    <h1 class="product-title">
      <span class="title-main">IRON</span>
      <span class="title-sub">TEMPO</span>
    </h1>
    <p class="product-type">Performance MultiVitamin</p>

    <p class="quality">PREMIUM QUALITY</p>
    <svg class="quality-stars" width="190" height="32" viewBox="0 0 190 32" aria-label="Five stars">
      <defs>
        <polygon id="star" points="16,1 20,11.5 31,12 22.5,19 25.5,30 16,24 6.5,30 9.5,19 1,12 12,11.5" fill="#ffffff"/>
      </defs>
      <use href="#star" x="0"/>
      <use href="#star" x="39"/>
      <use href="#star" x="78"/>
      <use href="#star" x="117"/>
      <use href="#star" x="156"/>
    </svg>

    <div class="count-badge">
      <span class="count-number">90</span>
      <span class="count-unit">tablets</span>
    </div>
    <p class="supplement-note">DIETARY SUPLEMENT</p>
  </section>
</div>
</body>
</html>
```